Plakat-Design für Immobilienmakler und Baufinanzierer
Zielgruppe
Wir sind Immobilienmakler und Baufinanzierer und suchen ein hochwertiges Design, unsere Zielgruppe sind Kunden, die Ihr Haus verkaufen möchten. Für jeden erfolgreichen Verkauf spenden wir 5 % unserer Maklercourtage an einen Verein, den sich der Kunde aussuchen darf. Mit diesem Plakat wollen wir auf unsere Vereinsförderng aufmerksam machen und Vereine ansprechen.
Aufgabenstellung
Text: 'Wir spenden 5 % unserer Provision für Ihren Verein', 'Nur 1,99 % Maklercourtage', Logo, Kontaktdaten

```html
<!DOCTYPE html>
<html lang="de">
<head>
<meta charset="utf-8">
<title>Brandau Immobilien – Vereinsförderung</title>
<link rel="stylesheet" href="https://fonts.googleapis.com/css2?family=Montserrat:wght@400;500;600;700;800;900&display=swap">
<style>
  :root {
    --teal: #1d6c7c;
    --teal-band: rgba(27, 104, 120, 0.88);
    --red: #972b33;
    --red-light: #d63a46;
    --white: #ffffff;
    --ink: #4a4a4a;
    --stage: #e4e4e4;
  }
  * { margin: 0; padding: 0; box-sizing: border-box; }
  html, body {
    width: 1200px; height: 1177px; overflow: hidden;
    background: var(--stage);
    font-family: "Montserrat", sans-serif;
  }
  .poster {
    position: absolute; left: 198px; top: 20px;
    width: 804px; height: 1137px;
    background: var(--white);
    overflow: hidden;
  }
  .hero-photo {
    position: absolute; left: 0; top: 0; width: 804px; height: 913px;
    background: linear-gradient(180deg, #5da9df 0%, #8fbfdc 14%, #d7b58c 32%, #c9a47c 52%, #a99a88 70%, #9c8d7b 84%, #7f8a5a 100%);
  }
  .teal-band {
    position: absolute; left: 197px; top: 0; width: 410px; height: 913px;
    background: var(--teal-band);
  }
  .brand-box {
    position: absolute; left: 218px; top: 0; width: 369px; height: 180px;
    background: var(--white);
    border-radius: 0 0 22px 22px;
    display: flex; align-items: center; justify-content: center; gap: 10px;
  }
  .brand-box .mark { width: 16px; height: 16px; background: var(--teal); }
  .brand-box .name {
    color: var(--teal); font-weight: 700; font-size: 24px; letter-spacing: 1px;
  }
  .headline { position: absolute; left: 197px; width: 410px; text-align: center; color: var(--white);
    text-shadow: 0 3px 8px rgba(0,0,0,0.25); white-space: nowrap; line-height: 1; }
  .headline.intro { top: 203px; font-size: 60px; font-weight: 800; }
  .headline.percent { top: 268px; font-size: 262px; font-weight: 900; letter-spacing: -6px; }
  .headline.unserer { top: 474px; font-size: 78px; font-weight: 800; }
  .headline.provision { top: 542px; font-size: 76px; font-weight: 800; }
  .headline.verein { top: 610px; font-size: 38px; font-weight: 500; }
  .offer-badge {
    position: absolute; left: 253px; top: 674px; width: 298px; height: 298px; border-radius: 50%;
    background: radial-gradient(circle at 50% 20%, var(--red-light) 0%, var(--red) 55%, var(--red) 100%);
    color: var(--white); text-align: center; line-height: 1;
  }
  .offer-badge .lead { position: absolute; top: 64px; width: 100%; font-size: 48px; font-weight: 500; }
  .offer-badge .rate { position: absolute; top: 112px; width: 100%; font-size: 84px; font-weight: 900; letter-spacing: -2px; }
  .offer-badge .label { position: absolute; top: 203px; width: 100%; font-size: 25px; font-weight: 600; }
  .contact { position: absolute; left: 71px; top: 958px; color: var(--ink); font-weight: 500; font-size: 16px; }
  .contact .company { color: var(--teal); font-weight: 700; font-size: 16px; margin-bottom: 12px; }
  .contact .row { display: flex; align-items: center; height: 36px; }
  .contact .item { display: flex; align-items: center; gap: 20px; }
  .contact .item.wide { width: 192px; }
  .contact svg { width: 18px; height: 18px; flex: none; }
  .footer-brand {
    position: absolute; left: 596px; top: 1046px;
    display: flex; align-items: center; gap: 8px;
    color: var(--teal); font-weight: 700; font-size: 16px;
  }
  .footer-brand .mark { width: 14px; height: 14px; background: var(--teal); }
</style>
</head>
<body>
<main class="poster">
  <div class="hero-photo" role="img" aria-label="Foto eines beleuchteten Einfamilienhauses mit Garage und Vorgarten in der Abenddämmerung"></div>
  <div class="teal-band"></div>

  <header class="brand-box">
    <span class="mark"></span>
    <span class="name">BRANDAU IMMOBILIEN</span>
  </header>

  <h1 class="headline intro">Wir spenden</h1>
  <div class="headline percent">5%</div>
  <div class="headline unserer">unserer</div>
  <div class="headline provision">Provision</div>
  <div class="headline verein">für Ihren Verein</div>

  <div class="offer-badge">
    <div class="lead">Nur</div>
    <div class="rate">1,99%</div>
    <div class="label">Maklercourtage</div>
  </div>

  <section class="contact">
    <div class="company">BRANDAU IMMOBILIEN</div>
    <div class="row">
      <span class="item">
        <svg viewBox="0 0 20 20"><path d="M10 1a7 7 0 0 0-7 7c0 5 7 11 7 11s7-6 7-11a7 7 0 0 0-7-7z" fill="#1d6c7c"/><circle cx="10" cy="8" r="2.6" fill="#fff"/></svg>
        AHORNSTR. 7 47800 WALLBACH
      </span>
    </div>
    <div class="row">
      <span class="item wide">
        <svg viewBox="0 0 20 20"><circle cx="10" cy="10" r="10" fill="#1d6c7c"/><path d="M6.5 5.5l2 0 1 2.5-1.3 1a6 6 0 0 0 2.8 2.8l1-1.3 2.5 1v2a1 1 0 0 1-1 1A8.5 8.5 0 0 1 5.5 6.5a1 1 0 0 1 1-1z" fill="#fff"/></svg>
        02151 000 12 34
      </span>
      <span class="item">
        <svg viewBox="0 0 20 20"><circle cx="10" cy="10" r="10" fill="#1d6c7c"/><rect x="5" y="6.5" width="10" height="7" rx="1" fill="none" stroke="#fff" stroke-width="1.3"/><path d="M5 7l5 4 5-4" fill="none" stroke="#fff" stroke-width="1.3"/></svg>
        INFO@BRANDAU-IMMOBILIEN.DE
      </span>
    </div>
    <div class="row">
      <span class="item wide">
        <svg viewBox="0 0 20 20"><rect x="5" y="1.5" width="10" height="17" rx="2" fill="none" stroke="#1d6c7c" stroke-width="2" transform="rotate(-25 10 10)"/><circle cx="12.5" cy="15" r="1.1" fill="#1d6c7c"/></svg>
        0160 000 123 45
      </span>
      <span class="item">
        <svg viewBox="0 0 20 20"><circle cx="10" cy="10" r="10" fill="#1d6c7c"/><circle cx="10" cy="10" r="5.5" fill="none" stroke="#fff" stroke-width="1.2"/><ellipse cx="10" cy="10" rx="2.3" ry="5.5" fill="none" stroke="#fff" stroke-width="1.2"/><path d="M4.5 10h11" stroke="#fff" stroke-width="1.2"/></svg>
        WWW.BRANDAU-IMMOBILIEN.DE
      </span>
    </div>
  </section>

  <div class="footer-brand">
    <span class="mark"></span>
    <span>BRANDAU</span>
  </div>
</main>
</body>
</html>
```